Online Consultancy Needs a New Logo & Business Card Design

Based on the new logo we just received from another contest here on Maketrove,

You'll find a few different versions of our logo as well as examples of business card designs we like in this folder:
==> https://share.plumvault.net/folderview?id=7Kq2WzTn4pLrXcv9BsHaYe1MoD5g&usp=sharing

We are considering two options:
- clean, black design
- clean, white/blue design

We're willing to consider both options.

We're considering adding some special effects to the cards when printing - emboss, rounded corners, etc.

However, please deliver a design WITHOUT round corners.

Target Market(s)

Successful business people, serious and older audience.

Industry/Entity Type

Business

Contact Information for Business Card

For the business card, I would like a minimalistic card with the logo on one side (perhaps in the middle) and the contact information on the other.

For the contact information please use:
Name: Peter Lund
Position: Founder
Email: peter.lund@korvim.com
Phone Number: +381 63 98 76 210
Website URL: www.korvim.com

Font styles to use
Serif
Sans Serif

Requirements
Must have
• Must fit in perfectly with our current website design.

```html
<!DOCTYPE html>
<html lang="en">
<head>
<meta charset="utf-8">
<title>Korvim Business Card</title>
<link href="https://fonts.googleapis.com/css2?family=PT+Sans:wght@400;700&display=swap" rel="stylesheet">
<style>
  :root {
    --stage: #ecebe8;
    --card-edge: #050505;
    --card-dark: #2f3335;
    --card-blue: #4ea2d3;
    --band: #0b0b0b;
    --ink: #16222b;
    --white: #ffffff;
    --accent: #4ea2d3;
  }
  * { margin: 0; padding: 0; box-sizing: border-box; }
  html, body { width: 1200px; height: 972px; overflow: hidden; }
  body {
    background: var(--stage);
    font-family: "PT Sans", sans-serif;
    position: relative;
  }
  .card-front {
    position: absolute;
    left: 186px; top: 30px;
    width: 362px; height: 916px;
    background: var(--card-edge);
    padding: 16px;
  }
  .card-front .surface {
    width: 100%; height: 100%;
    background: var(--card-dark);
    position: relative;
  }
  .brand {
    position: absolute;
    left: 0; right: 0; top: 372px;
    display: flex; align-items: center; justify-content: center; gap: 16px;
    color: var(--accent);
    font-size: 64px;
    font-weight: 700;
    letter-spacing: 1px;
  }
  .brand .mark {
    width: 34px; height: 34px; border-radius: 50%;
    background: var(--accent);
  }
  .card-back {
    position: absolute;
    left: 648px; top: 30px;
    width: 364px; height: 900px;
    background: var(--card-blue);
    overflow: hidden;
  }
  .name {
    position: absolute; left: 52px; top: 96px;
    font-size: 56px; color: var(--ink); line-height: 1;
  }
  .rule {
    position: absolute; left: 52px; top: 176px;
    width: 282px; height: 2px; background: var(--ink);
  }
  .role {
    position: absolute; left: 84px; top: 182px;
    font-size: 40px; color: var(--ink); line-height: 1.1;
  }
  .web-band {
    position: absolute; left: 0; top: 346px;
    width: 100%; height: 76px; background: var(--band);
    display: flex; align-items: center; justify-content: center;
    color: var(--white); font-size: 40px;
  }
  .contact-band {
    position: absolute; left: 0; top: 736px;
    width: 100%; height: 164px; background: var(--band);
    color: var(--white);
  }
  .phone {
    position: absolute; left: 18px; top: 30px;
    display: flex; align-items: center; gap: 12px;
    font-size: 30px;
  }
  .phone svg { width: 26px; height: 42px; }
  .email {
    position: absolute; left: 0; right: 0; top: 100px;
    text-align: center; font-size: 30px;
  }
</style>
</head>
<body>
  <section class="card-front">
    <div class="surface">
      <div class="brand"><span class="mark"></span><span>korvim</span></div>
    </div>
  </section>

  <section class="card-back">
    <h1 class="name" style="font-weight:400">Peter Lund</h1>
    <div class="rule"></div>
    <p class="role">Founder</p>
    <div class="web-band">www.korvim.com</div>
    <div class="contact-band">
      <div class="phone">
        <svg viewBox="0 0 26 42" aria-hidden="true">
          <rect x="2" y="2" width="22" height="38" rx="4" fill="var(--accent)"/>
          <rect x="6" y="8" width="14" height="14" fill="var(--band)"/>
          <rect x="6" y="26" width="14" height="10" fill="var(--band)" opacity="0.6"/>
        </svg>
        <span>+381 63 98 76 210</span>
      </div>
      <p class="email">peter.lund@korvim.com</p>
    </div>
  </section>
</body>
</html>
```